Harbor Vantage needs new design business card

We are video surveillance and analytics software development company.
I am looking for a professional business card.
Our website is www.harborvantage-example.com.au
Please have a loo and get the feel for who we are and what we do.
I do not know what else to give you apart from good luck and I hope your design gets selected.
Thank you very much for participating
Industry/Entity Type
Business
Contact Information for Business Card
Address
27/14 Pemberly Street Millbrook NSW 2199
Telephone 1300 582 741
Mobile 0450 713 258
email: marcus@harborvantage-example.com.au
name
Marcus Felder
Position
Managing Director
Font styles to use
Other font styles liked:
- Arial
Look and feel

```html
<!DOCTYPE html>
<html lang="en">
<head>
<meta charset="utf-8">
<title>Harbor Vantage – Business Card</title>
<link rel="stylesheet" href="https://fonts.googleapis.com/css2?family=Arimo:wght@400;700&display=swap">
<style>
  :root {
    --navy: #1d4580;
    --navy-deep: #163764;
    --steel: #6f8ea6;
    --grey-text: #6b6f75;
    --paper: #ffffff;
    --backdrop: #e9eaec;
  }
  html, body {
    margin: 0;
    padding: 0;
    width: 1200px;
    height: 1023px;
    overflow: hidden;
    background: var(--backdrop);
    font-family: "Arimo", Arial, sans-serif;
  }
  .sheet {
    position: relative;
    width: 1200px;
    height: 1023px;
  }
  .card {
    position: absolute;
    left: 180px;
    width: 840px;
    height: 480px;
    overflow: hidden;
    box-shadow: 0 6px 18px rgba(0,0,0,0.18);
  }
  .card--front { top: 21px; background: var(--paper); }
  .card--back {
    top: 522px;
    background: linear-gradient(135deg, #24508f 0%, var(--navy) 45%, var(--navy-deep) 100%);
  }
  .card svg.waves { position: absolute; inset: 0; z-index: 0; }

  .wordmark {
    position: absolute;
    z-index: 1;
    display: flex;
    align-items: center;
    gap: 16px;
    font-weight: 700;
    letter-spacing: 1px;
    text-transform: uppercase;
    white-space: nowrap;
  }
  .wordmark__square { width: 38px; height: 38px; }
  .card--front .wordmark { left: 60px; top: 140px; color: var(--navy); font-size: 40px; }
  .card--front .wordmark__square { background: var(--navy); }
  .card--back .wordmark { left: 0; right: 0; top: 205px; justify-content: center; color: var(--paper); font-size: 52px; }
  .card--back .wordmark__square { background: var(--paper); width: 48px; height: 48px; }

  .person {
    position: absolute;
    z-index: 1;
    right: 110px;
    top: 34px;
    text-align: right;
    white-space: nowrap;
  }
  .person__name { color: var(--navy); font-weight: 700; font-size: 30px; }
  .person__role { color: var(--grey-text); font-size: 16px; margin-top: 4px; }

  .contacts {
    position: absolute;
    z-index: 1;
    left: 38px;
    bottom: 18px;
    color: var(--paper);
    font-size: 18px;
    line-height: 26px;
    white-space: nowrap;
  }
  .contacts__row { display: flex; align-items: center; gap: 12px; }
  .contacts__row svg { width: 16px; height: 16px; flex: none; }
  .contacts__address { font-weight: 700; font-size: 20px; margin-top: 4px; }

  .site-line {
    position: absolute;
    left: 40px;
    right: 40px;
    bottom: 40px;
    display: flex;
    align-items: center;
    gap: 14px;
    color: var(--paper);
    font-size: 17px;
  }
  .site-line__rule { height: 1px; background: rgba(255,255,255,0.8); }
  .site-line__rule--short { width: 60px; }
  .site-line__rule--long { flex: 1; }
</style>
</head>
<body>
<main class="sheet">

  <section class="card card--front" aria-label="Card front">
    <svg class="waves" viewBox="0 0 840 480" preserveAspectRatio="none" aria-hidden="true">
      <path d="M0,285 C220,280 420,245 560,190 C680,150 770,100 840,70 L840,92 C770,120 680,172 560,212 C420,270 220,305 0,310 Z" fill="var(--steel)"/>
      <path d="M0,316 C220,311 420,276 560,218 C680,178 770,126 840,98 L840,480 L0,480 Z" fill="var(--navy)"/>
      <path d="M0,313 C220,308 420,273 560,215 C680,175 770,123 840,95" fill="none" stroke="#ffffff" stroke-width="3"/>
    </svg>

    <div class="wordmark"><span class="wordmark__square"></span>Harbor Vantage</div>

    <div class="person">
      <div class="person__name">Marcus Felder</div>
      <div class="person__role">Managing Director</div>
    </div>

    <div class="contacts">
      <div class="contacts__row">
        <svg viewBox="0 0 16 16"><rect x="1" y="5" width="14" height="10" rx="1" fill="#fff"/><rect x="4" y="1" width="8" height="4" fill="#fff"/></svg>
        1300 582 741
      </div>
      <div class="contacts__row">
        <svg viewBox="0 0 16 16"><rect x="4" y="1" width="8" height="14" rx="1.5" fill="none" stroke="#fff" stroke-width="1.6"/><circle cx="8" cy="12.5" r="1" fill="#fff"/></svg>
        0450 713 258
      </div>
      <div class="contacts__row">
        <svg viewBox="0 0 16 16"><rect x="1" y="3" width="14" height="10" fill="none" stroke="#fff" stroke-width="1.6"/><path d="M1,3 L8,9 L15,3" fill="none" stroke="#fff" stroke-width="1.6"/></svg>
        marcus@harborvantage-example.com.au
      </div>
      <div class="contacts__row">
        <svg viewBox="0 0 16 16"><rect x="1" y="2" width="14" height="9" fill="none" stroke="#fff" stroke-width="1.6"/><rect x="5" y="13" width="6" height="1.6" fill="#fff"/></svg>
        www.harborvantage-example.com.au
      </div>
      <div class="contacts__address">27/14 Pemberly Street Millbrook NSW 2199</div>
    </div>
  </section>

  <section class="card card--back" aria-label="Card back">
    <div class="wordmark"><span class="wordmark__square"></span>Harbor Vantage</div>
    <div class="site-line">
      <span class="site-line__rule site-line__rule--short"></span>
      <span>www.harborvantage-example.com.au</span>
      <span class="site-line__rule site-line__rule--long"></span>
    </div>
  </section>

</main>
</body>
</html>
```